Domain Parking page and Listing page

1)
In need a design of a domain parking page, mainly with the same features as VORIQ.com as can be seen here: https://wanderplum.com/

2)
I need a design of a website with all domains listed. There's no company logo/name yet so it should be in plain font, for example "tilmorex.site" (this is just an example), similar as:
https://voriq.com/search?&terms=park&results=50&order_by=relevance

Delivery after approval in HTML/CSS. Should be responsive. Ideally use a framework like Bootstrap

Target Market(s)

Domain buyers, business owners

Industry/Entity Type

Business to business, Marketing, domains

Coding

Coded - Design and coding required

Number of Pages Required

2 page

Font styles to use
Sans Serif

Requirements
Must have
• Responsive design, worldly design.

```html
<!DOCTYPE html>
<html lang="en">
<head>
<meta charset="utf-8">
<title>Stallora.Com – Search Online Business For Sale</title>
<link href="https://fonts.googleapis.com/css2?family=Outfit:wght@300;400;500;600&display=swap" rel="stylesheet">
<style>
:root{
  --navy:#020a36;
  --blue-deep:#0b2284;
  --blue-mid:#1236a8;
  --link:#1a36c8;
  --green:#11c47b;
  --green-soft:#e8faf2;
  --ink:#0d1440;
  --text:#2b2f45;
  --muted:#6f7488;
  --line:#c9ccd6;
  --tint:#f4f8fd;
  --tint-head:#eef4fc;
  --white:#fff;
}
*{box-sizing:border-box;margin:0;padding:0}
html,body{width:1200px;height:2246px;overflow:hidden}
body{font-family:"Outfit",sans-serif;color:var(--text);background:var(--white);position:relative}
.hero{position:absolute;left:0;top:0;width:1200px;height:377px;
  background:linear-gradient(115deg,var(--blue-deep) 0%,var(--blue-mid) 45%,#0a2590 70%,var(--blue-deep) 100%)}
.hero::before{content:"";position:absolute;left:0;top:0;width:100%;height:78px;background:var(--navy)}
.site-header{position:absolute;left:107px;top:37px;width:986px;height:76px;background:var(--white);
  display:flex;align-items:center;padding:0 14px 0 18px}
.brand{display:flex;align-items:center;gap:12px;font-weight:600;font-size:28px;color:var(--ink)}
.brand-dot{width:34px;height:34px;border-radius:50%;background:var(--link)}
.nav{margin-left:auto;display:flex;align-items:center;gap:53px;font-size:15px;color:var(--ink)}
.login{margin-left:34px;width:102px;height:49px;border:2px solid var(--green);background:var(--green-soft);
  color:var(--green);font-weight:500;font-size:15px;display:flex;align-items:center;justify-content:center}
.hero-title{position:absolute;left:0;width:1200px;top:180px;text-align:center;color:var(--white);font-size:34px;font-weight:500}
.search{position:absolute;left:321px;top:245px;width:558px;height:58px;background:var(--white);display:flex;align-items:center;padding-left:23px}
.search span{font-size:12px;color:var(--muted)}
.search-btn{position:absolute;right:10px;top:8px;width:87px;height:43px;background:var(--green);color:var(--white);
  font-weight:500;font-size:15px;display:flex;align-items:center;justify-content:center}
.section-title{position:absolute;left:0;width:1200px;top:437px;text-align:center;font-size:27px;font-weight:500;color:var(--ink)}
.count{position:absolute;left:108px;top:510px;font-size:15px;color:var(--ink);font-weight:500}
.sort-label{position:absolute;left:852px;top:510px;font-size:15px;color:var(--ink);font-weight:500}
.sort{position:absolute;left:920px;top:496px;width:160px;height:49px;border:1px solid var(--line);display:flex;align-items:center;
  padding:0 17px;font-size:15px;color:var(--ink);justify-content:space-between}
.filters{position:absolute;left:106px;top:561px;width:291px;height:1187px;border:1px solid #e6e9f0}
.f-head{height:51px;background:var(--tint-head);display:flex;align-items:center;justify-content:space-between;padding:0 18px 0 16px;
  font-size:15px;color:var(--link)}
.f-body{padding:16px 16px 0}
.check{display:flex;align-items:center;gap:13px;font-size:13.5px;color:var(--text);height:36px}
.box{width:21px;height:20px;border:1px solid #555;border-radius:2px;flex:none}
.ext-add{display:flex;gap:4px;margin-top:10px}
.ext-add .inp{width:211px;height:45px;border:1px solid var(--line);font-size:13.5px;display:flex;align-items:center;padding-left:13px}
.ext-add .plus{width:44px;height:45px;background:#e3effd;color:var(--link);font-size:22px;display:flex;align-items:center;justify-content:center}
.range{display:flex;align-items:center;gap:5px;font-size:13.5px}
.sel{width:118px;height:45px;border:1px solid var(--line);display:flex;align-items:center;justify-content:space-between;padding:0 9px 0 11px}
.slider{position:relative;height:14px;margin-top:8px}
.slider::before{content:"";position:absolute;left:4px;right:0;top:6px;height:2px;background:var(--link)}
.slider::after{content:"";position:absolute;left:0;top:0;width:13px;height:13px;border-radius:50%;background:var(--link)}
.txt{height:45px;border:1px solid var(--line);margin-top:-8px;width:256px}
.results{position:absolute;left:414px;top:561px;width:665px;height:1196px;border:1px solid #e1e5ee}
.row{position:relative;display:flex;align-items:center;padding:0 20px 0 26px}
.row:nth-child(odd){background:var(--tint)}
.row-info{flex:1}
.domain{font-size:18px;font-weight:500;color:var(--link);margin-bottom:8px}
.meta{display:flex;font-size:11.5px;line-height:18px}
.meta div{width:87px}
.meta div:nth-child(2){width:105px}
.meta .k{color:var(--muted)}
.meta .v{color:var(--ink)}
.btn{width:122px;height:43px;display:flex;align-items:center;justify-content:center;font-size:16px;font-weight:500;margin-top:-20px}
.btn-solid{background:var(--green);color:var(--white)}
.btn-line{border:1px solid var(--green);color:var(--green);background:var(--white)}
.pager{position:absolute;top:1838px;left:0;width:1200px;font-size:13px;color:var(--ink)}
.pager span{position:absolute}
.help{position:absolute;left:0;top:1918px;width:1200px;height:258px;background:#f7f9fe}
.help h2{position:absolute;left:0;width:1200px;top:66px;text-align:center;font-size:27px;font-weight:500;color:var(--ink)}
.contact{position:absolute;top:128px;display:flex;align-items:center;gap:19px;font-size:18px;color:var(--ink);font-weight:500}
.ico{width:63px;height:63px;border-radius:50%;background:#e4eefc;display:flex;align-items:center;justify-content:center}
.footer{position:absolute;left:0;top:2176px;width:1200px;height:70px;background:var(--navy);color:var(--white);
  display:flex;align-items:center;justify-content:center;font-size:13.5px;gap:18px}
</style>
</head>
<body>
<div class="hero"></div>
<header class="site-header">
  <div class="brand"><span class="brand-dot"></span>Stallora.Com</div>
  <nav class="nav"><span>Buy Domain</span><span>Sell Domain</span><span>Leran</span><span>Company</span></nav>
  <div class="login">Log In</div>
</header>
<h1 class="hero-title">Search Online Business For Sale</h1>
<div class="search"><span>park</span><div class="search-btn">Search</div></div>

<h2 class="section-title">Get Your Domain</h2>
<div class="count">For Sale (5,923)</div>
<div class="sort-label">Sort by :</div>
<div class="sort">Most Relevant
  <svg width="11" height="7" viewBox="0 0 11 7"><path d="M1 1l4.5 4.5L10 1" fill="none" stroke="#0d1440" stroke-width="1.4"/></svg>
</div>

<aside class="filters">
  <div class="f-head">Categories<svg width="13" height="8" viewBox="0 0 13 8"><path d="M1 7l5.5-5.5L12 7" fill="none" stroke="#1a36c8" stroke-width="1.6"/></svg></div>
  <div class="f-body" style="height:131px;padding-top:12px">
    <div class="check"><span class="box"></span>Popular Domain Names</div>
    <div class="check"><span class="box"></span>3-letter Domain Names</div>
    <div class="check"><span class="box"></span>Premium Domain Names</div>
  </div>
  <div class="f-head">Extensions<svg width="13" height="8" viewBox="0 0 13 8"><path d="M1 7l5.5-5.5L12 7" fill="none" stroke="#1a36c8" stroke-width="1.6"/></svg></div>
  <div class="f-body" style="height:195px;padding-top:12px">
    <div class="check"><span class="box"></span>.com</div>
    <div class="check"><span class="box"></span>.net</div>
    <div class="check"><span class="box"></span>.org</div>
    <div class="ext-add"><div class="inp">add extension</div><div class="plus">+</div></div>
  </div>
  <div class="f-head">Length<svg width="13" height="8" viewBox="0 0 13 8"><path d="M1 7l5.5-5.5L12 7" fill="none" stroke="#1a36c8" stroke-width="1.6"/></svg></div>
  <div class="f-body" style="height:112px;padding-top:20px">
    <div class="range"><div class="sel">1<svg width="9" height="6" viewBox="0 0 9 6"><path d="M1 1l3.5 3.5L8 1" fill="none" stroke="#333" stroke-width="1.2"/></svg></div>to<div class="sel">50<svg width="9" height="6" viewBox="0 0 9 6"><path d="M1 1l3.5 3.5L8 1" fill="none" stroke="#333" stroke-width="1.2"/></svg></div></div>
    <div class="slider"></div>
  </div>
  <div class="f-head">Price<svg width="13" height="8" viewBox="0 0 13 8"><path d="M1 7l5.5-5.5L12 7" fill="none" stroke="#1a36c8" stroke-width="1.6"/></svg></div>
  <div class="f-body" style="height:103px;padding-top:20px">
    <div class="range"><div class="sel">0<svg width="9" height="6" viewBox="0 0 9 6"><path d="M1 1l3.5 3.5L8 1" fill="none" stroke="#333" stroke-width="1.2"/></svg></div>to<div class="sel">10000<svg width="9" height="6" viewBox="0 0 9 6"><path d="M1 1l3.5 3.5L8 1" fill="none" stroke="#333" stroke-width="1.2"/></svg></div></div>
    <div class="slider"></div>
  </div>
  <div class="f-head">Name<svg width="13" height="8" viewBox="0 0 13 8"><path d="M1 7l5.5-5.5L12 7" fill="none" stroke="#1a36c8" stroke-width="1.6"/></svg></div>
  <div class="f-body" style="height:132px;padding-top:12px">
    <div class="check"><span class="box"></span>No hyphen</div>
    <div class="check"><span class="box"></span>No numerals</div>
    <div class="check"><span class="box"></span>No special chars</div>
  </div>
  <div class="f-head">Starting With<svg width="13" height="8" viewBox="0 0 13 8"><path d="M1 7l5.5-5.5L12 7" fill="none" stroke="#1a36c8" stroke-width="1.6"/></svg></div>
  <div class="f-body" style="height:79px;padding-top:13px"><div class="txt"></div></div>
  <div class="f-head">Ending With<svg width="13" height="8" viewBox="0 0 13 8"><path d="M1 7l5.5-5.5L12 7" fill="none" stroke="#1a36c8" stroke-width="1.6"/></svg></div>
  <div class="f-body" style="height:73px;padding-top:16px"><div class="txt"></div></div>
</aside>

<section class="results">
  <div class="row" style="height:121px"><div class="row-info"><div class="domain">Parksoftwaresourcing.com</div><div class="meta"><div><span class="k">Type</span><br><span class="v">Domain</span></div><div><span class="k">Domain Age</span><br><span class="v">20 years</span></div><div><span class="k">Industry</span><br><span class="v">Internet</span></div></div></div><div class="btn btn-solid" style="margin-top:-10px">View Listing</div></div>
  <div class="row" style="height:125px"><div class="row-info"><div class="domain">Parkloremipsum.com</div><div class="meta"><div><span class="k">Type</span><br><span class="v">Domain</span></div><div><span class="k">Domain Age</span><br><span class="v">20 years</span></div><div><span class="k">Industry</span><br><span class="v">Internet</span></div></div></div><div class="btn btn-line" style="margin-top:-10px">Make Offer</div></div>
  <div class="row" style="height:126px"><div class="row-info"><div class="domain">Parkdummy.com</div><div class="meta"><div><span class="k">Type</span><br><span class="v">Domain</span></div><div><span class="k">Domain Age</span><br><span class="v">20 years</span></div><div><span class="k">Industry</span><br><span class="v">Internet</span></div></div></div><div class="btn btn-line" style="margin-top:-10px">Make Offer</div></div>
  <div class="row" style="height:135px"><div class="row-info"><div class="domain">Parkdomain.com</div><div class="meta"><div><span class="k">Type</span><br><span class="v">Domain</span></div><div><span class="k">Domain Age</span><br><span class="v">20 years</span></div><div><span class="k">Industry</span><br><span class="v">Internet</span></div></div></div><div class="btn btn-line" style="margin-top:-10px">Make Offer</div></div>
  <div class="row" style="height:126px"><div class="row-info"><div class="domain">Parkdomain.com</div><div class="meta"><div><span class="k">Type</span><br><span class="v">Domain</span></div><div><span class="k">Domain Age</span><br><span class="v">20 years</span></div><div><span class="k">Industry</span><br><span class="v">Internet</span></div></div></div><div class="btn btn-line" style="margin-top:-10px">Make Offer</div></div>
  <div class="row" style="height:157px"><div class="row-info"><div class="domain">Parkdomain.com</div><div class="meta"><div><span class="k">Type</span><br><span class="v">Domain</span></div><div><span class="k">Domain Age</span><br><span class="v">20 years</span></div><div><span class="k">Industry</span><br><span class="v">Internet</span></div></div></div><div class="btn btn-line" style="margin-top:-10px">Make Offer</div></div>
  <div class="row" style="height:126px"><div class="row-info"><div class="domain">parkmelnor.com</div><div class="meta"><div><span class="k">Type</span><br><span class="v">Domain</span></div><div><span class="k">Domain Age</span><br><span class="v">20 years</span></div><div><span class="k">Industry</span><br><span class="v">Internet</span></div></div></div><div class="btn btn-line" style="margin-top:-10px">Make Offer</div></div>
  <div class="row" style="height:154px"><div class="row-info"><div class="domain">Parksoftwaresourcing.com</div><div class="meta"><div><span class="k">Type</span><br><span class="v">Domain</span></div><div><span class="k">Domain Age</span><br><span class="v">20 years</span></div><div><span class="k">Industry</span><br><span class="v">Internet</span></div></div></div><div class="btn btn-solid" style="margin-top:-10px">View Listing</div></div>
  <div class="row" style="height:124px"><div class="row-info"><div class="domain">loremipsum.com</div><div class="meta"><div><span class="k">Type</span><br><span class="v">Domain</span></div><div><span class="k">Domain Age</span><br><span class="v">20 years</span></div><div><span class="k">Industry</span><br><span class="v">Internet</span></div></div></div><div class="btn btn-line" style="margin-top:-10px">Make Offer</div></div>
</section>

<nav class="pager">
  <span style="left:459px"><svg width="7" height="11" viewBox="0 0 7 11"><path d="M6 1L1.5 5.5 6 10" fill="none" stroke="#0d1440" stroke-width="1.3"/></svg></span>
  <span style="left:506px;color:var(--link)">1</span>
  <span style="left:540px">2</span>
  <span style="left:579px">3</span>
  <span style="left:615px">4</span>
  <span style="left:651px">5</span>
  <span style="left:669px">......</span>
  <span style="left:696px">130</span>
  <span style="left:735px"><svg width="7" height="11" viewBox="0 0 7 11"><path d="M1 1l4.5 4.5L1 10" fill="none" stroke="#1a36c8" stroke-width="1.3"/></svg></span>
</nav>

<section class="help">
  <h2>Questions?We’re happy to help</h2>
  <div class="contact" style="left:383px">
    <span class="ico"><svg width="28" height="28" viewBox="0 0 24 24"><path fill="#1a36c8" d="M6.6 10.8c1.4 2.8 3.8 5.1 6.6 6.6l2.2-2.2c.3-.3.7-.4 1-.2 1.1.4 2.3.6 3.6.6.6 0 1 .4 1 1V20c0 .6-.4 1-1 1C10.6 21 3 13.4 3 4c0-.6.4-1 1-1h3.5c.6 0 1 .4 1 1 0 1.3.2 2.5.6 3.6.1.3 0 .7-.2 1z"/></svg></span>
    +1 - 123-456-7890
  </div>
  <div class="contact" style="left:676px">
    <span class="ico"><svg width="26" height="20" viewBox="0 0 26 20"><rect x="1" y="1" width="24" height="18" fill="none" stroke="#1a36c8" stroke-width="2"/><path d="M1 1l12 10L25 1M1 19l9-8M25 19l-9-8" fill="none" stroke="#1a36c8" stroke-width="2"/></svg></span>
    Write Us
  </div>
</section>

<footer class="footer">
  <span>Terms &amp; Conditions</span><span>I</span><span>Contact Us</span><span>I</span><span>Copyright© 2023,All Right Reserved</span>
</footer>
</body>
</html>
```